Marlowe Ridge Holdings

I have a real estate investment business.

** I need editable vector files of the final design.

Industry/Entity Type

Real Estate

Contact Information for Business Card

I would like the card to be clear and direct with the company name and contact info. I would prefer not to have a design that is too busy (i.e., with excessive detail) in the business card.

Font styles to use
Sans Serif

Requirements
Must have
• My card must have the following information listed below:
• Company name: Marlowe Ridge Holdings LLC
• My name: Daniel Vestrap
• Phone number: (555) 218-9064
• Email address: dlvestrap@fernmail.example
• Keywords: “Real Estate Investments”
Nice to have
• I would like to have a design that resembles the characteristics/uses of obsidian stone which resembles something related to strength and resilience. Perhaps something with sharp, sleek color transitions as well.

```html
<!DOCTYPE html>
<html lang="en">
<head>
<meta charset="utf-8">
<title>Marlowe Ridge Holdings LLC — Business Card</title>
<link rel="stylesheet" href="https://fonts.googleapis.com/css2?family=Arimo:ital,wght@0,400;0,700;1,400&family=Cormorant+Garamond:wght@700&display=swap">
<style>
  :root {
    --backdrop: #2b2b2b;
    --front-band: #ffcbcb;
    --back-face: #fdd9cc;
    --paper: #ffffff;
    --ember: #f25a27;
    --charcoal: #3a3a3a;
    --ink: #2d1f14;
    --text: #1e1e1e;
  }
  * { box-sizing: border-box; margin: 0; padding: 0; }
  html, body { width: 1200px; height: 987px; overflow: hidden; }
  body { background: var(--backdrop); position: relative; font-family: "Arimo", Arial, sans-serif; }

  .card {
    position: absolute; left: 284px; width: 633px; height: 361px;
    border-radius: 19px; overflow: hidden;
  }
  .card--front { top: 102px; background: var(--paper); }
  .card--back { top: 539px; background: var(--back-face); }

  .brand { display: flex; align-items: center; justify-content: center; gap: 14px; }
  .brand__mark { width: 42px; height: 42px; background: var(--charcoal); border-radius: 6px; flex: none; }
  .brand__name {
    color: var(--ember); font-weight: 400; text-transform: uppercase;
    letter-spacing: 3px; white-space: nowrap;
  }

  .front__band {
    position: absolute; left: 0; top: 0; width: 100%; height: 148px;
    background: var(--front-band);
  }
  .front__band .brand { height: 100%; }
  .front__band .brand__name { font-size: 24px; }

  .holder {
    position: absolute; left: 42px; top: 170px; width: 565px;
    display: flex; align-items: baseline; gap: 20px;
  }
  .holder__name {
    font-family: "Cormorant Garamond", Georgia, serif; font-weight: 700;
    font-size: 26px; letter-spacing: 3.5px; color: var(--ink); text-transform: uppercase;
  }
  .holder__phone { font-style: italic; font-size: 23px; color: var(--text); }
  .holder__rule {
    position: absolute; left: 38px; top: 213px; width: 569px; height: 2px;
    background: linear-gradient(90deg, var(--charcoal) 0 47%, var(--ember) 47% 100%);
  }

  .contacts {
    position: absolute; left: 48px; top: 232px; width: 560px;
    display: grid; grid-template-columns: 266px 1fr; row-gap: 8px;
    list-style: none;
  }
  .contacts__item { display: flex; align-items: center; gap: 8px; font-size: 16px; color: var(--text); white-space: nowrap; }
  .contacts__dot { width: 15px; height: 15px; border-radius: 50%; background: var(--ember); flex: none; }

  .front__footer { position: absolute; left: 0; top: 300px; width: 633px; height: 61px; }
  .front__tagline {
    position: absolute; right: 12px; top: 325px; font-style: italic;
    font-size: 17px; letter-spacing: 0.5px; color: var(--paper); white-space: nowrap;
  }

  .card--back .brand { height: 100%; }
  .card--back .brand__mark { width: 50px; height: 50px; }
  .card--back .brand__name { font-size: 27px; }
</style>
</head>
<body>
  <section class="card card--front" aria-label="Business card front">
    <header class="front__band">
      <div class="brand">
        <span class="brand__mark"></span>
        <span class="brand__name">Marlowe Ridge Holdings LLC</span>
      </div>
    </header>

    <div class="holder">
      <span class="holder__name">Daniel Vestrap</span>
      <span class="holder__phone">(555) 218-9064</span>
    </div>
    <div class="holder__rule"></div>

    <ul class="contacts">
      <li class="contacts__item"><span class="contacts__dot"></span>@fernbook.example</li>
      <li class="contacts__item"><span class="contacts__dot"></span>@chirpline.example</li>
      <li class="contacts__item"><span class="contacts__dot"></span>@snapframe.example</li>
      <li class="contacts__item"><span class="contacts__dot"></span>dlvestrap@fernmail.example</li>
    </ul>

    <svg class="front__footer" viewBox="0 300 633 61" width="633" height="61" aria-hidden="true">
      <path d="M352 349 L378 316 L633 316 L633 361 L340 361 Z" fill="var(--ember)"/>
      <rect x="0" y="341" width="362" height="5" fill="var(--charcoal)"/>
      <rect x="0" y="352" width="633" height="9" fill="var(--ember)"/>
    </svg>
    <p class="front__tagline">Real Estate Investments</p>
  </section>

  <section class="card card--back" aria-label="Business card back">
    <div class="brand">
      <span class="brand__mark"></span>
      <span class="brand__name">Marlowe Ridge Holdings LLC</span>
    </div>
  </section>
</body>
</html>
```